New Business cards design and layout
Verant cards
New Business cards design and layout - Information Technology
Creative Brief
Professional
Dorian T. Halvek
VP, Sales and Business Development
4718 - 12th Avenue N.W. Calgary, Alberta T3K 1R8
dorian@verantinfo.ca
www.verantinfo.ca

```html
<!DOCTYPE html>
<html lang="en">
<head>
<meta charset="utf-8">
<title>Verant – Business Card</title>
<link rel="stylesheet" href="https://fonts.googleapis.com/css2?family=Exo+2:wght@500;600&family=Open+Sans:wght@400&display=swap">
<style>
  :root {
    --brand-blue: #1a55c9;
    --brand-blue-dark: #0f3f9e;
    --accent-red: #8e1b2c;
    --card-white: #ffffff;
    --card-shade: #eceef1;
    --text-dark: #2e3238;
    --icon-blue: #1f5ccc;
  }
  * { margin: 0; padding: 0; box-sizing: border-box; }
  html, body {
    width: 1200px;
    height: 816px;
    overflow: hidden;
    background: var(--card-white);
  }
  .business-card {
    position: relative;
    width: 1200px;
    height: 816px;
    background: linear-gradient(180deg, var(--card-white) 0%, var(--card-white) 70%, var(--card-shade) 100%);
    font-family: "Open Sans", Arial, sans-serif;
    color: var(--text-dark);
  }
  .brand {
    position: absolute;
    left: 790px;
    top: 96px;
    display: flex;
    align-items: center;
    gap: 22px;
  }
  .brand-square {
    width: 64px;
    height: 64px;
    background: var(--brand-blue);
  }
  .brand-name {
    font-family: "Exo 2", Arial, sans-serif;
    font-weight: 600;
    font-size: 66px;
    letter-spacing: 2px;
    color: var(--brand-blue);
    line-height: 1;
  }
  .divider-line {
    position: absolute;
    left: 0;
    top: 0;
  }
  .name-band {
    position: absolute;
    left: 0;
    top: 388px;
    width: 600px;
    height: 122px;
    background: linear-gradient(90deg, var(--brand-blue-dark), var(--brand-blue));
    border-radius: 0 61px 61px 0;
    color: var(--card-white);
    text-align: right;
    padding: 20px 62px 0 0;
  }
  .person-name {
    font-family: "Exo 2", Arial, sans-serif;
    font-weight: 500;
    font-size: 46px;
    line-height: 1.1;
  }
  .person-title {
    font-family: "Exo 2", Arial, sans-serif;
    font-weight: 500;
    font-size: 20px;
    letter-spacing: 1px;
    margin-top: 8px;
    white-space: nowrap;
  }
  .contact-list {
    position: absolute;
    left: 78px;
    top: 624px;
    list-style: none;
  }
  .contact-item {
    display: flex;
    align-items: center;
    gap: 20px;
    height: 58px;
    font-size: 28px;
  }
  .contact-icon { width: 26px; height: 26px; fill: var(--icon-blue); flex-shrink: 0; }
  .address {
    position: absolute;
    left: 750px;
    top: 560px;
    display: flex;
    gap: 18px;
    font-size: 28px;
    line-height: 1.35;
  }
  .address .contact-icon { margin-top: 6px; }
</style>
</head>
<body>
<div class="business-card">
  <div class="brand">
    <div class="brand-square"></div>
    <div class="brand-name">VERANT</div>
  </div>

  <svg class="divider-line" width="1200" height="816" viewBox="0 0 1200 816" aria-hidden="true">
    <line x1="1200" y1="232" x2="560" y2="400" stroke="var(--accent-red)" stroke-width="3"/>
  </svg>

  <div class="name-band">
    <div class="person-name">Dorian T. Halvek</div>
    <div class="person-title">VP, SALES AND BUSINESS DEVELOPMENT</div>
  </div>

  <ul class="contact-list">
    <li class="contact-item">
      <svg class="contact-icon" viewBox="0 0 24 24" aria-hidden="true"><path d="M2 5h20v14H2z M3.5 6.5 12 13l8.5-6.5" stroke="#fff" stroke-width="1.4"/></svg>
      <span>dorian@verantinfo.ca</span>
    </li>
    <li class="contact-item">
      <svg class="contact-icon" viewBox="0 0 24 24" aria-hidden="true"><circle cx="12" cy="12" r="10"/><path d="M2 12h20M12 2c3 3 3 17 0 20M12 2c-3 3-3 17 0 20M4 7h16M4 17h16" stroke="#fff" stroke-width="1.2" fill="none"/></svg>
      <span>www.verantinfo.ca</span>
    </li>
  </ul>

  <div class="address">
    <svg class="contact-icon" viewBox="0 0 24 24" aria-hidden="true"><path d="M12 3 2 12h3v9h5v-6h4v6h5v-9h3z"/></svg>
    <div>4718 - 12th Avenue N.W.,<br>Calgary, Alberta T3K 1R8</div>
  </div>
</div>
</body>
</html>
```